Amber Ridge LLC Business Cards and Stationary
Amber Ridge LLC
Simple
Marcus Delford
C.E.O.
42 Tamarind Ct Stanton, CA, 90712
Marcus@amberridgeLLC.com
www.amberridgellc.com www.amberridgeproperty.com
I would like the front to be very clean, maybe only the logo, and maybe management and Real Estate Services
On the back of the card i would like all the information to leave a clean and organized look. Instead of Using Fax: written out i would prefer F:

```html
<!DOCTYPE html>
<html lang="en">
<head>
<meta charset="utf-8">
<title>Amber Ridge LLC Business Card</title>
<link href="https://fonts.googleapis.com/css2?family=Open+Sans:wght@400;600;700&display=swap" rel="stylesheet">
<style>
  :root {
    --backdrop: #d9d9db;
    --card-white: #ffffff;
    --card-edge: #f1f2f4;
    --navy: #22388c;
    --sky: #2f8fd8;
    --teal: #2a8aa8;
    --logo-dot: #2fa3b8;
    --ink-light: #ffffff;
  }
  * { box-sizing: border-box; margin: 0; padding: 0; }
  html, body {
    width: 1200px; height: 902px; overflow: hidden;
    background: var(--backdrop);
    font-family: "Open Sans", Arial, sans-serif;
  }
  .canvas { position: relative; width: 1200px; height: 902px; }

  .card {
    position: absolute; width: 600px; height: 343px;
    background: var(--card-white);
    box-shadow: 0 6px 18px rgba(0,0,0,0.18);
    overflow: hidden;
  }
  .card-front { left: 130px; top: 80px; background: linear-gradient(160deg, var(--card-white), var(--card-edge)); }
  .card-back { left: 470px; top: 480px; }

  .brand {
    position: absolute; display: flex; align-items: center; gap: 10px;
    color: var(--teal); font-weight: 600; font-size: 24px; letter-spacing: 0.5px;
    white-space: nowrap;
  }
  .brand-dot { width: 22px; height: 22px; border-radius: 50%; background: var(--logo-dot); }
  .card-front .brand { left: 50%; top: 50%; transform: translate(-50%, -50%); }
  .card-back .brand { left: 36px; top: 160px; font-size: 21px; }

  .back-shapes { position: absolute; inset: 0; width: 600px; height: 343px; }

  .contact {
    position: absolute; right: 30px; top: 36px;
    color: var(--ink-light); text-align: right;
  }
  .contact-name { font-size: 19px; font-weight: 700; }
  .contact-role { font-size: 15px; margin-bottom: 26px; }
  .contact-line {
    display: flex; justify-content: flex-end; align-items: center; gap: 8px;
    font-size: 14px; line-height: 23px;
  }
  .contact-line svg { width: 13px; height: 13px; fill: var(--ink-light); }
</style>
</head>
<body>
<div class="canvas">

  <section class="card card-front">
    <div class="brand"><span class="brand-dot"></span>Amber Ridge LLC</div>
  </section>

  <section class="card card-back">
    <svg class="back-shapes" viewBox="0 0 600 343" aria-hidden="true">
      <defs>
        <linearGradient id="arcBand" x1="0" y1="0" x2="1" y2="1">
          <stop offset="0" stop-color="#5bc0ee"/>
          <stop offset="1" stop-color="#1f6fc4"/>
        </linearGradient>
      </defs>
      <rect width="600" height="343" fill="var(--navy)"/>
      <path d="M0 0 H250 C372 70 372 262 200 343 H0 Z" fill="url(#arcBand)"/>
      <path d="M0 0 H232 C352 66 350 258 180 343 H0 Z" fill="var(--card-white)"/>
    </svg>

    <div class="brand"><span class="brand-dot"></span>Amber Ridge LLC</div>

    <div class="contact">
      <div class="contact-name">Lena Harrow</div>
      <div class="contact-role">Consultant</div>
      <div class="contact-line">42 Tamarind Ct</div>
      <div class="contact-line">Stanton, CA 90712
        <svg viewBox="0 0 16 16"><path d="M3.5 1l2.5 3-1.6 1.6c.9 2 2.5 3.6 4.5 4.5L10.5 8.5l3 2.5-1.5 3C6.5 14 2 9.5 2 3.5z"/></svg>
      </div>
      <div class="contact-line">555 214 0387
        <svg viewBox="0 0 16 16"><path d="M5 1h6a1 1 0 0 1 1 1v12a1 1 0 0 1-1 1H5a1 1 0 0 1-1-1V2a1 1 0 0 1 1-1zm0 2v9h6V3z"/></svg>
      </div>
      <div class="contact-line">Marcus@amberridgeLLC.com
        <svg viewBox="0 0 16 16"><path d="M1 3h14v10H1zm1.5 1.2L8 8.5l5.5-4.3z"/></svg>
      </div>
      <div class="contact-line">www.amberridgellc.com</div>
    </div>
  </section>

</div>
</body>
</html>
```